Brightfield Co Trade Show Flyer

We need a brochure design (8.5 x 11) Info in the design (refer to rough draft I drew on Paper): "#1 selling tool to aquire new franchisees has been video testimonials" - Martin L. Crowe, C.E.O Tovik Smoothie Franchise Testimonials - Let your franchisees do the selling for you. Franchisee testimonial: $10,000 / per Franchisee Includes: • 2 minute Video • 1 minute add for your franchise's location • Concept creation • Communication with franchisee • Travel to their location • All rental equipment • 1 round of corrections • Animated logo • Licensed music ******* For 25% Discount section (next to middle box), please put the "Outlet Summit Logo" Great to use on all your social media (USE logos and icons) • Website • Vidstream • Linkwork • Facenote • Snapgram • Chirper • Phone calls • Emails • In person meetings Some of our clients: (use the logos I uploaded - in round boxes as in draft) LOGO (Brightfield Franchise Testimonial) www.brightfieldvoices.example (866) 555-0172

Target Market(s)

Franchise owners

Colors

Designer to choose colors to be used in the design.

Requirements

```html
<!DOCTYPE html>
<html lang="en">
<head>
<meta charset="utf-8">
<title>Brightfield Franchise Testimonials – Trade Show Flyer</title>
<link rel="stylesheet" href="https://fonts.googleapis.com/css2?family=Archivo+Black&family=Titillium+Web:wght@300;400;600;700&display=swap">
<style>
  :root{
    --charcoal:#3f3f41;
    --charcoal-deep:#353537;
    --orange:#f7941d;
    --orange-dark:#b5560f;
    --orange-light:#fbb040;
    --white:#ffffff;
    --paper:#f3f3f4;
    --ink:#111111;
    --teal:#0fa58c;
    --rule:#c9c9cc;
  }
  *{box-sizing:border-box;margin:0;padding:0}
  html,body{width:970px;height:1200px;overflow:hidden;background:var(--paper)}
  body{font-family:"Titillium Web",sans-serif;color:var(--white)}
  .flyer{position:relative;width:970px;height:1200px;background:var(--paper)}
  .hero{position:absolute;left:0;top:0;width:970px;height:902px;background:var(--charcoal)}
  .quote{position:absolute;top:30px;width:100%;text-align:center;font-size:31px;font-weight:600;letter-spacing:.2px}
  .attribution{position:absolute;top:80px;width:100%;text-align:center;font-size:23px;font-weight:300}
  .attribution strong{font-weight:600}
  .headline{position:absolute;left:0;width:100%;text-align:center;font-family:"Archivo Black",sans-serif;font-size:98px;line-height:1;
    background:linear-gradient(100deg,var(--orange-dark) 0%,var(--orange) 30%,var(--orange-dark) 55%,var(--orange-light) 80%,var(--orange) 100%);
    -webkit-background-clip:text;background-clip:text;color:transparent;filter:drop-shadow(4px 5px 5px rgba(0,0,0,.45))}
  .headline.line1{top:140px;letter-spacing:-1px}
  .headline.line2{top:243px;letter-spacing:-2px}
  .tagline-band{position:absolute;left:121px;top:354px;width:730px;height:40px;
    background:linear-gradient(90deg,#7a3a0c 0%,var(--orange-dark) 30%,var(--orange) 70%,var(--orange-dark) 100%);
    font-size:31px;font-weight:600;line-height:40px;text-align:center;letter-spacing:.3px}
  .package{position:absolute;left:119px;top:430px;width:547px;height:277px;border:11px solid var(--white);background:var(--charcoal);
    box-shadow:inset 0 0 0 1px #666;padding:4px 0 0 27px}
  .package h2{font-size:26px;font-weight:600;color:var(--orange);line-height:38px}
  .package ul{list-style:none}
  .package li{display:flex;align-items:center;font-size:18px;font-weight:300;line-height:26.6px}
  .tick{width:13px;height:13px;margin-right:9px;flex:none}
  .discount-badge{position:absolute;left:696px;top:430px;width:155px;height:181px;background:var(--white);color:var(--ink);
    clip-path:polygon(0 0,100% 0,100% 100%,50% 91%,0 100%);text-align:center}
  .discount-badge .pct{font-family:"Archivo Black",sans-serif;font-size:56px;line-height:1;margin-top:8px;letter-spacing:-2px}
  .discount-badge .for{font-size:21px;font-weight:300;line-height:1.1}
  .partner-name{display:flex;align-items:center;justify-content:center;gap:6px;margin-top:14px;font-size:19px;font-weight:700;color:var(--teal);line-height:1}
  .partner-name .mark{width:12px;height:12px;background:var(--teal)}
  .discount-badge .chevron{position:absolute;left:0;bottom:0;width:155px;height:18px}
  .reaction-photo{position:absolute;left:662px;top:621px;width:245px;height:281px;border-radius:120px 120px 0 0;
    background:linear-gradient(180deg,#6b4030 0%,#b9805f 45%,#d9a98a 75%,#e9e4e0 100%)}
  .channels{position:absolute;left:119px;top:777px;width:552px;height:97px;border:1px solid var(--rule);border-top:none}
  .channels::before,.channels::after{content:"";position:absolute;top:0;height:1px;background:var(--rule)}
  .channels::before{left:0;width:101px}
  .channels::after{right:0;width:101px}
  .channels h3{position:absolute;top:-15px;left:0;width:100%;text-align:center;font-size:19px;font-weight:600;color:var(--orange);letter-spacing:.3px}
  .channel-row{position:absolute;left:18px;top:38px;display:flex;gap:13px}
  .channel{width:45px;text-align:center}
  .channel .tile{width:34px;height:34px;margin:0 auto;border-radius:6px;background:var(--orange);display:flex;align-items:center;justify-content:center}
  .channel .name{display:block;font-size:9px;font-weight:600;color:var(--orange);line-height:14px;white-space:nowrap}
  .brand-block{position:absolute;left:60px;top:940px;width:340px;text-align:center;color:var(--ink)}
  .brand-name{display:flex;align-items:center;justify-content:center;gap:12px;font-size:44px;font-weight:700;letter-spacing:1px;line-height:1}
  .brand-name .dot{width:38px;height:38px;border-radius:50%;background:var(--ink)}
  .brand-sub{margin-top:10px;font-size:13px;font-weight:700;letter-spacing:.4px}
  .brand-sub::before,.brand-sub::after{content:" — ";color:#777;font-weight:300}
  .phone{margin-top:16px;font-size:24px;font-weight:700;color:var(--orange)}
  .web{font-size:23px;font-weight:700;line-height:1.1}
  .clients{position:absolute;left:481px;top:950px;width:435px;height:213px;border:1px solid var(--rule);border-top:none}
  .clients::before,.clients::after{content:"";position:absolute;top:0;height:1px;background:var(--rule)}
  .clients::before{left:0;width:130px}
  .clients::after{right:0;width:130px}
  .clients h3{position:absolute;top:-15px;width:100%;text-align:center;font-size:19px;font-weight:600;color:var(--orange)}
  .client{position:absolute;display:flex;align-items:center;gap:6px;font-size:15px;font-weight:700;color:var(--ink);white-space:nowrap}
  .client .mark{width:14px;height:14px;border-radius:50%;background:var(--orange)}
  .footer-strip{position:absolute;left:0;bottom:0;width:970px;height:10px;background:var(--charcoal)}
</style>
</head>
<body>
<main class="flyer">
  <section class="hero">
    <p class="quote">#1 selling tool to aquire new franchisees</p>
    <p class="attribution"><strong>Dana Hollis,</strong> Ceo Crispo Grill</p>
    <h1 class="headline line1">FRANCHISEE</h1>
    <h1 class="headline line2" aria-hidden="true">TESTIMONIAL</h1>
    <div class="tagline-band">LET YOUR FRANCHISEES DO THE SELLING...</div>

    <div class="package">
      <h2>$10,000 / per testimonials</h2>
      <ul>
        <li><svg class="tick" viewBox="0 0 14 14"><circle cx="7" cy="7" r="7" fill="#f7941d"/><path d="M3.5 7.2l2.4 2.4 4.6-5" stroke="#7a3a0c" stroke-width="1.6" fill="none"/></svg>2 minute video</li>
        <li><svg class="tick" viewBox="0 0 14 14"><circle cx="7" cy="7" r="7" fill="#f7941d"/><path d="M3.5 7.2l2.4 2.4 4.6-5" stroke="#7a3a0c" stroke-width="1.6" fill="none"/></svg>1 minute add for your franchise's location</li>
        <li><svg class="tick" viewBox="0 0 14 14"><circle cx="7" cy="7" r="7" fill="#f7941d"/><path d="M3.5 7.2l2.4 2.4 4.6-5" stroke="#7a3a0c" stroke-width="1.6" fill="none"/></svg>Concept creation</li>
        <li><svg class="tick" viewBox="0 0 14 14"><circle cx="7" cy="7" r="7" fill="#f7941d"/><path d="M3.5 7.2l2.4 2.4 4.6-5" stroke="#7a3a0c" stroke-width="1.6" fill="none"/></svg>Communication with franchisee</li>
        <li><svg class="tick" viewBox="0 0 14 14"><circle cx="7" cy="7" r="7" fill="#f7941d"/><path d="M3.5 7.2l2.4 2.4 4.6-5" stroke="#7a3a0c" stroke-width="1.6" fill="none"/></svg>Travel to their location</li>
        <li><svg class="tick" viewBox="0 0 14 14"><circle cx="7" cy="7" r="7" fill="#f7941d"/><path d="M3.5 7.2l2.4 2.4 4.6-5" stroke="#7a3a0c" stroke-width="1.6" fill="none"/></svg>All rental equipment</li>
        <li><svg class="tick" viewBox="0 0 14 14"><circle cx="7" cy="7" r="7" fill="#f7941d"/><path d="M3.5 7.2l2.4 2.4 4.6-5" stroke="#7a3a0c" stroke-width="1.6" fill="none"/></svg>1 round of corrections</li>
        <li><svg class="tick" viewBox="0 0 14 14"><circle cx="7" cy="7" r="7" fill="#f7941d"/><path d="M3.5 7.2l2.4 2.4 4.6-5" stroke="#7a3a0c" stroke-width="1.6" fill="none"/></svg>Animated logo</li>
      </ul>
    </div>

    <div class="discount-badge">
      <p class="pct">25%</p>
      <p class="for">Discount For</p>
      <p class="partner-name"><span class="mark"></span>The Outlet Summit</p>
      <svg class="chevron" viewBox="0 0 155 18" preserveAspectRatio="none"><polyline points="0,18 77.5,4 155,18" fill="none" stroke="#f7941d" stroke-width="3"/></svg>
    </div>

    <div class="reaction-photo" role="img" aria-label="Photo of a surprised young woman with long brown hair, hands raised beside her face"></div>

    <div class="channels">
      <h3>USE TESTIMONIALS EVERYWHERE</h3>
      <div class="channel-row">
        <div class="channel"><span class="tile"></span><span class="name">Facenote</span></div>
        <div class="channel"><span class="tile"></span><span class="name">Vidstream</span></div>
        <div class="channel"><span class="tile"></span><span class="name">Snapgram</span></div>
        <div class="channel"><span class="tile"></span><span class="name">Linkwork</span></div>
        <div class="channel"><span class="tile"></span><span class="name">Chirper</span></div>
        <div class="channel"><span class="tile"><svg width="24" height="18" viewBox="0 0 24 18"><rect x="1" y="1" width="22" height="16" rx="2" fill="none" stroke="#3f3f41" stroke-width="2"/><polyline points="1,2 12,10 23,2" fill="none" stroke="#3f3f41" stroke-width="2"/></svg></span><span class="name">Email</span></div>
        <div class="channel"><span class="tile"><svg width="24" height="24" viewBox="0 0 24 24" fill="none" stroke="#3f3f41" stroke-width="1.8"><circle cx="12" cy="12" r="10"/><ellipse cx="12" cy="12" rx="4.5" ry="10"/><line x1="2" y1="12" x2="22" y2="12"/><line x1="3.5" y1="7" x2="20.5" y2="7"/><line x1="3.5" y1="17" x2="20.5" y2="17"/></svg></span><span class="name">Website</span></div>
        <div class="channel"><span class="tile"><svg width="22" height="22" viewBox="0 0 24 24"><path d="M6.6 2.5l3 4-2 2.5c1.3 2.8 3.6 5.1 6.4 6.4l2.5-2 4 3-1.8 4c-9.5.3-17.2-7.4-16.9-16.9z" fill="#3f3f41"/></svg></span><span class="name">Phone</span></div>
        <div class="channel"><span class="tile"><svg width="24" height="22" viewBox="0 0 24 22" fill="#3f3f41"><circle cx="6" cy="5" r="3"/><circle cx="18" cy="5" r="3"/><circle cx="12" cy="9" r="3"/><rect x="3" y="9" width="6" height="9" rx="2"/><rect x="15" y="9" width="6" height="9" rx="2"/><rect x="9" y="13" width="6" height="9" rx="2"/></svg></span><span class="name">Meetings</span></div>
      </div>
    </div>
  </section>

  <section class="brand-block">
    <p class="brand-name"><span class="dot"></span>BRIGHTFIELD</p>
    <p class="brand-sub">FRANCHISE TESTIMONIALS</p>
    <p class="phone">(866) 555-0172</p>
    <p class="web">www.brightfieldvoices.example</p>
  </section>

  <section class="clients">
    <h3>TRUSTED BY</h3>
    <p class="client" style="left:95px;top:60px"><span class="mark"></span>Scoopwell</p>
    <p class="client" style="left:230px;top:60px"><span class="mark"></span>Tovik Smoothie</p>
    <p class="client" style="left:40px;top:150px"><span class="mark"></span>Corner 24</p>
    <p class="client" style="left:165px;top:150px"><span class="mark"></span>Tidyline</p>
    <p class="client" style="left:285px;top:150px"><span class="mark"></span>Axleworks</p>
  </section>

  <div class="footer-strip"></div>
</main>
</body>
</html>
```